B.P.L.H. Letterhead design

I would like a really professionally designed letterhead for my professional tutoring business called "The Bright Pathway Learning House" (B.P.L.H.).Something fresh,modern and inspiring that will breath new life into the bu.The business/centre offers professional tutoring for 6 - 16 year olds in maths and english.

I have also attached a centre picture our logo, our proposed school bag,and our latest newsletter to give some perspective & background.

We like to see designs that use the blue & yellow colour theme.The final design should communicate ... "Giving Your Child A Secure Future ... And You Yourself ... Peace Of Mind!!!"

```html
<!DOCTYPE html>
<html lang="en">
<head>
<meta charset="utf-8">
<title>B.P.L.H. Letterhead</title>
<link href="https://fonts.googleapis.com/css2?family=Arimo:wght@400&family=Marcellus&display=swap" rel="stylesheet">
<style>
  :root {
    --navy: #16306a;
    --yellow: #f6c200;
    --ink: #58595b;
    --frame: #8a8a8a;
    --paper: #ffffff;
  }
  html, body { margin: 0; padding: 0; overflow: hidden; background: var(--paper); }
  .letterhead {
    position: relative;
    width: 849px;
    height: 1200px;
    box-sizing: border-box;
    border: 1px solid var(--frame);
    background: var(--paper);
    overflow: hidden;
    font-family: "Arimo", Arial, sans-serif;
  }
  .side-bands { position: absolute; left: 0; top: 0; }
  .brand {
    position: absolute;
    right: 71px;
    top: 121px;
    text-align: center;
    color: var(--navy);
  }
  .brand-name {
    margin: 0;
    font-family: "Marcellus", serif;
    font-weight: 400;
    font-size: 15px;
    line-height: 18px;
  }
  .brand-tagline {
    margin: 3px auto 0;
    padding-top: 2px;
    width: 190px;
    border-top: 1px solid var(--navy);
    font-family: "Marcellus", serif;
    font-size: 8px;
    line-height: 10px;
  }
  .letter-body {
    position: absolute;
    left: 98px;
    top: 262px;
    width: 652px;
    color: var(--ink);
    font-size: 16.4px;
    line-height: 23.5px;
  }
  .salutation { margin: 0 0 48px; }
  .letter-body p.text { margin: 0 0 23.5px; text-align: justify; }
  .footer {
    position: absolute;
    right: 70px;
    top: 1113px;
    text-align: right;
    color: var(--navy);
  }
  .footer-name {
    margin: 0 0 8px;
    font-family: "Marcellus", serif;
    font-weight: 400;
    font-size: 16.5px;
  }
  .footer-contact {
    margin: 0;
    font-size: 11px;
    line-height: 16px;
  }
</style>
</head>
<body>
<div class="letterhead">
  <svg class="side-bands" width="849" height="1200" viewBox="0 0 849 1200">
    <defs>
      <linearGradient id="centre-photo-tones" x1="0" y1="0" x2="0" y2="1">
        <stop offset="0" stop-color="#8fa3b8"/>
        <stop offset="0.5" stop-color="#b9a58a"/>
        <stop offset="1" stop-color="#c79456"/>
      </linearGradient>
    </defs>
    <path class="navy-band" fill="var(--navy)"
          d="M0,0 H93 C74,220 60,480 61,700 C62,900 72,1060 88,1200 H0 Z"/>
    <path class="yellow-band" fill="var(--yellow)"
          d="M66,380 C60,700 92,1000 168,1200 H95 C80,1060 69,900 68,700 C67,560 66,460 66,380 Z"/>
    <ellipse class="centre-photo" role="img" aria-label="Photo of the learning centre classroom with computer desks"
             cx="133" cy="104" rx="85" ry="54"
             fill="url(#centre-photo-tones)" stroke="#ffffff" stroke-width="5"/>
  </svg>

  <div class="brand">
    <p class="brand-name">BrightPathwayLearningHouse.co.uk</p>
    <p class="brand-tagline">London's Leading Learning Centre</p>
  </div>

  <main class="letter-body">
    <p class="salutation">Dear Sir,</p>
    <p class="text">Lorem Ipsum is simply dummy text of the printing and typesetting industry. Lorem Ipsum has been the industry's standard dummy text ever since the 1500s, when an unknown printer took a galley of type and scrambled it to make a type specimen book. It has survived not only five centuries, but also the leap into electronic typesetting, remaining essentially unchanged. It was popularised in the 1960s with the release of Typeline sheets containing Lorem Ipsum passages, and more recently with desktop publishing software like Orrin PageBuilder including versions of Lorem Ipsum.</p>
    <p class="text">Lorem Ipsum is simply dummy text of the printing and typesetting industry. Lorem Ipsum has been the industry's standard dummy text ever since the 1500s, when an unknown printer took a galley of type and scrambled it to make a type specimen book. It has survived not only five centuries, but also the leap into electronic typesetting, remaining essentially unchanged. It was popularised in the 1960s with the release of Typeline sheets containing Lorem Ipsum passages, and more recently with desktop publishing software like Orrin PageBuilder including versions of Lorem Ipsum.</p>
    <p class="text">Lorem Ipsum is simply dummy text of the printing and typesetting industry. Lorem Ipsum has been the industry's standard dummy text ever since the 1500s, when an unknown printer took a galley of type and scrambled it to make a type specimen book.</p>
  </main>

  <footer class="footer">
    <p class="footer-name">The Bright Pathway Learning House</p>
    <p class="footer-contact">Add.:&nbsp; Your Commercial or office address • Ph.: 00.00.00.0000 • Fax: 00.00.00.0000<br>
    Email: yourname@yourwebsite.com • Web.: www.yourwebsite.com</p>
  </footer>
</div>
</body>
</html>
```